Real estate for sale A-frame sign

I have a vision but do not know any software tools. I need to create a real estate sign from scratch. The sign is traditionally a 4:5 ratio--more tall than wide. The text needed on the sign is governed by California state law, so that is not a variable. The font, font size and colors used are the variables.

The red and gold sample has the exact text needed.
Updates

The text on the sign should be like the red and gold sample I included in my brief. Unsure why some designers are putting "governed by state law" on the sign. ??? And can we elevate the font to something more sophisticated? I included both the Lantern and marlowe's logos for inspiration. The fonts used should be similar.

Target Market(s)

sophisticated homeowners

Font styles to use
Serif
Sans Serif

Colors
0455a3
cedeed
ec1f27
ffffff
fbed22
fdf9cf

Requirements
Must have
• An elevated sense of style and class. Look to Lantern real estate and marlowe's real estate for their logo and font styles.
Nice to have
• I have a need for a:

A baccarat red background and gold text
A navy blue background with light blue text
A navy blue background with pale yellow text
A deep forest green background with white text

```html
<!DOCTYPE html>
<html lang="en">
<head>
<meta charset="utf-8">
<title>For Sale Sign – Colour Variations</title>
<link rel="stylesheet" href="https://fonts.googleapis.com/css2?family=Playfair+Display:ital,wght@0,400;0,700;1,700&family=Poppins:wght@600&display=swap">
<style>
  :root {
    --page-bg: #ffffff;
    --stage-bg: #eceee8;
    --baccarat: #7f0f02;
    --gold: #f4d27a;
    --navy: #002a5a;
    --sky: #7ab6f5;
    --pale-yellow: #fbe122;
    --forest: #0d3a03;
    --white: #ffffff;
  }
  * { margin: 0; padding: 0; box-sizing: border-box; }
  html, body { width: 1200px; height: 2427px; overflow: hidden; background: var(--page-bg); }
  body { position: relative; }

  .hero-stage {
    position: absolute; left: 0; top: 0; width: 1200px; height: 1151px;
    background: var(--stage-bg);
  }

  .sign {
    position: absolute;
    aspect-ratio: 4 / 5;
    background: var(--sign-bg);
    color: var(--sign-ink);
    overflow: hidden;
  }
  .sign--hero { left: 400px; top: 219px; width: 574px; font-size: 5.74px; }
  .sign--small { width: 410px; font-size: 4.1px; }
  .sign--a { left: 141px; top: 1257px; }
  .sign--b { left: 600px; top: 1257px; }
  .sign--c { left: 141px; top: 1810px; }
  .sign--d { left: 600px; top: 1810px; }

  .theme-red   { --sign-bg: var(--baccarat); --sign-ink: var(--gold); }
  .theme-sky   { --sign-bg: var(--navy); --sign-ink: var(--sky); }
  .theme-lemon { --sign-bg: var(--navy); --sign-ink: var(--pale-yellow); }
  .theme-pine  { --sign-bg: var(--forest); --sign-ink: var(--white); }

  .sign__texture {
    position: absolute; left: 0; top: 0; bottom: 0; width: 35%;
    background: linear-gradient(to right,
      color-mix(in srgb, var(--sign-ink) 30%, var(--sign-bg)) 0%,
      color-mix(in srgb, var(--sign-ink) 14%, var(--sign-bg)) 55%,
      color-mix(in srgb, var(--sign-ink) 6%, var(--sign-bg)) 100%);
  }

  .sign__line {
    position: absolute; left: 41.5%; transform: translateY(-50%);
    white-space: nowrap; line-height: 1;
  }
  .sign__title {
    top: 12.1%; font-family: "Playfair Display", serif; font-weight: 700; font-size: 13.2em;
  }
  .sign__governed {
    top: 40.7%; font-family: "Playfair Display", serif; font-style: italic; font-weight: 700; font-size: 5.4em;
  }
  .sign__law {
    top: 53.8%; font-family: "Playfair Display", serif; font-weight: 700; font-size: 10.4em; line-height: 1.02;
    letter-spacing: 0.01em;
  }
  .sign__rule {
    position: absolute; left: 41.5%; top: 64.9%; width: 48.8%; height: 0.3em; background: var(--sign-ink);
  }
  .sign__phone {
    top: 72.7%; font-family: "Poppins", sans-serif; font-weight: 600; font-size: 5.9em;
  }
  .sign__web {
    top: 90.8%; font-family: "Playfair Display", serif; font-weight: 400; font-size: 4.5em;
  }
</style>
</head>
<body>
  <div class="hero-stage"></div>

  <div class="sign sign--hero theme-red">
    <div class="sign__texture" role="img" aria-label="Halftone dot pattern fading toward the centre"></div>
    <p class="sign__line sign__title">For Sale</p>
    <p class="sign__line sign__governed">Governed By</p>
    <p class="sign__line sign__law">California<br>State Law</p>
    <div class="sign__rule"></div>
    <p class="sign__line sign__phone">0123 456 789</p>
    <p class="sign__line sign__web">www.yourweb.com</p>
  </div>

  <div class="sign sign--small sign--a theme-red">
    <div class="sign__texture" role="img" aria-label="Halftone dot pattern fading toward the centre"></div>
    <p class="sign__line sign__title">For Sale</p>
    <p class="sign__line sign__governed">Governed By</p>
    <p class="sign__line sign__law">California<br>State Law</p>
    <div class="sign__rule"></div>
    <p class="sign__line sign__phone">0123 456 789</p>
    <p class="sign__line sign__web">www.yourweb.com</p>
  </div>

  <div class="sign sign--small sign--b theme-sky">
    <div class="sign__texture" role="img" aria-label="Halftone dot pattern fading toward the centre"></div>
    <p class="sign__line sign__title">For Sale</p>
    <p class="sign__line sign__governed">Governed By</p>
    <p class="sign__line sign__law">California<br>State Law</p>
    <div class="sign__rule"></div>
    <p class="sign__line sign__phone">0123 456 789</p>
    <p class="sign__line sign__web">www.yourweb.com</p>
  </div>

  <div class="sign sign--small sign--c theme-lemon">
    <div class="sign__texture" role="img" aria-label="Halftone dot pattern fading toward the centre"></div>
    <p class="sign__line sign__title">For Sale</p>
    <p class="sign__line sign__governed">Governed By</p>
    <p class="sign__line sign__law">California<br>State Law</p>
    <div class="sign__rule"></div>
    <p class="sign__line sign__phone">0123 456 789</p>
    <p class="sign__line sign__web">www.yourweb.com</p>
  </div>

  <div class="sign sign--small sign--d theme-pine">
    <div class="sign__texture" role="img" aria-label="Halftone dot pattern fading toward the centre"></div>
    <p class="sign__line sign__title">For Sale</p>
    <p class="sign__line sign__governed">Governed By</p>
    <p class="sign__line sign__law">California<br>State Law</p>
    <div class="sign__rule"></div>
    <p class="sign__line sign__phone">0123 456 789</p>
    <p class="sign__line sign__web">www.yourweb.com</p>
  </div>
</body>
</html>
```